Agribusiness Insurance

I would like postcard designed to attract farmers and agribusiness owners to my insurance consulting services. My business model is being a Trusted Advisor through identifying exposures, developing strategies, implementing programs and then monitoring our designed plan. I am knowledge representative (13YRs ag insurance), Represent 15 Farm + Carriers (favorable pricing/competitive multiple options) Specialized in Confinements, Cattle Farms, and Grain Producers. No Membership Fees Necessary

Many Insurance Producers in my area are nearing retirement I am 33 and am looking to promote this..

Target Market(s)

Farmers and Agribusiness Owners

Industry/Entity Type

Agribusiness

Requirements
Must have

• Toby Halvern
Phone: Cell 555 207 4816
Email: thalvern@ruralplexadvice.example

```html
<!DOCTYPE html>
<html lang="en">
<head>
<meta charset="utf-8">
<title>Insuring Your Future Today – Agribusiness Insurance Postcard</title>
<link rel="stylesheet" href="https://fonts.googleapis.com/css2?family=Poppins:ital,wght@0,400;0,700;1,700&display=swap">
<style>
  :root {
    --paper: #ffffff;
    --ink: #111111;
    --text-dark: #2a2420;
    --orange: #ee7d12;
    --orange-bright: #f7901e;
    --red: #c21f33;
    --black-bar: #000000;
    --sky-top: #6c6a8e;
    --sky-mid: #e9a35a;
    --sky-glow: #f47a1c;
    --field-dark: #1d3318;
    --field-mid: #3c6a2c;
    --portrait-bg: #8a7f76;
  }
  * { box-sizing: border-box; margin: 0; padding: 0; }
  html, body {
    width: 1200px; height: 930px; overflow: hidden;
    background: var(--paper);
    font-family: "Poppins", Arial, sans-serif;
  }
  .postcard {
    position: absolute; left: 30px; top: 30px;
    width: 1140px; height: 868px; overflow: hidden;
  }
  .scene {
    position: absolute; inset: 0;
    background:
      linear-gradient(180deg,
        var(--sky-top) 0%,
        #a98c9a 10%,
        var(--sky-mid) 20%,
        #f5b03c 28%,
        var(--sky-glow) 34%,
        #e5673a 36.5%,
        #2c3a22 38%,
        var(--field-mid) 42%,
        #2f5a25 55%,
        var(--field-dark) 80%,
        #14240f 100%);
  }
  .headline {
    position: absolute; top: 88px; left: 0; width: 100%;
    text-align: center;
    font-weight: 700; font-size: 55px; letter-spacing: 0.5px;
    color: var(--ink);
    text-shadow:
      -2px -2px 0 #fff, 2px -2px 0 #fff, -2px 2px 0 #fff, 2px 2px 0 #fff,
      0 -2px 0 #fff, 0 2px 0 #fff, -2px 0 0 #fff, 2px 0 0 #fff,
      3px 4px 6px rgba(0,0,0,.5);
  }
  .benefits {
    position: absolute; left: 697px; top: 420px;
    list-style: none;
  }
  .benefits li {
    display: flex; align-items: center;
    height: 38.3px;
    font-weight: 700; font-style: italic; font-size: 22px;
    color: var(--orange-bright);
    text-shadow: 1px 1px 0 #3a1a00, 2px 2px 4px rgba(0,0,0,.7);
  }
  .benefits svg { width: 26px; height: 22px; margin-right: 14px; flex: none; }
  .swoosh { position: absolute; left: 0; top: 0; width: 1140px; height: 868px; }
  .portrait {
    position: absolute; left: 22px; top: 582px;
    width: 186px; height: 246px;
    border: 6px solid var(--paper);
    background: linear-gradient(180deg, #9a8f86 0%, var(--portrait-bg) 55%, #1c1c1c 100%);
    box-shadow: 2px 3px 6px rgba(0,0,0,.35);
  }
  .contact { position: absolute; left: 231px; top: 726px; color: var(--text-dark); }
  .contact-name { font-weight: 700; font-size: 31px; line-height: 1.1; color: #1a1410; }
  .contact-line { font-weight: 400; font-size: 22px; line-height: 1.45; }
  .footer-bar {
    position: absolute; left: 0; bottom: 0; width: 100%; height: 20px;
    background: var(--black-bar);
  }
</style>
</head>
<body>
  <main class="postcard">
    <div class="scene" role="img" aria-label="Photograph of a green soybean field under a vivid orange sunset sky"></div>

    <h1 class="headline">INSURING YOUR FUTURE... TODAY</h1>

    <ul class="benefits">
      <li><svg viewBox="0 0 26 22"><path d="M2 12 L9 19 L24 3" fill="none" stroke="var(--orange-bright)" stroke-width="3" stroke-linecap="round" stroke-linejoin="round"/></svg>Represent 15 Farm + Carriers</li>
      <li><svg viewBox="0 0 26 22"><path d="M2 12 L9 19 L24 3" fill="none" stroke="var(--orange-bright)" stroke-width="3" stroke-linecap="round" stroke-linejoin="round"/></svg>favorable pricing</li>
      <li><svg viewBox="0 0 26 22"><path d="M2 12 L9 19 L24 3" fill="none" stroke="var(--orange-bright)" stroke-width="3" stroke-linecap="round" stroke-linejoin="round"/></svg>competitive multiple options</li>
      <li><svg viewBox="0 0 26 22"><path d="M2 12 L9 19 L24 3" fill="none" stroke="var(--orange-bright)" stroke-width="3" stroke-linecap="round" stroke-linejoin="round"/></svg>Specialized in Confinements</li>
      <li><svg viewBox="0 0 26 22"><path d="M2 12 L9 19 L24 3" fill="none" stroke="var(--orange-bright)" stroke-width="3" stroke-linecap="round" stroke-linejoin="round"/></svg>Grain Producers</li>
      <li><svg viewBox="0 0 26 22"><path d="M2 12 L9 19 L24 3" fill="none" stroke="var(--orange-bright)" stroke-width="3" stroke-linecap="round" stroke-linejoin="round"/></svg>Cattle Farms</li>
      <li><svg viewBox="0 0 26 22"><path d="M2 12 L9 19 L24 3" fill="none" stroke="var(--orange-bright)" stroke-width="3" stroke-linecap="round" stroke-linejoin="round"/></svg>No Membership Fees</li>
    </ul>

    <svg class="swoosh" viewBox="0 0 1140 868" aria-hidden="true">
      <path d="M0 558 C280 548 440 600 600 680 C760 760 900 792 1140 728 L1140 780 C900 830 720 812 560 730 C410 650 250 582 0 582 Z" fill="var(--red)"/>
      <path d="M0 582 C250 582 410 650 560 730 C720 812 900 830 1140 780 L1140 848 L0 848 Z" fill="var(--orange)"/>
      <path d="M470 612 C640 700 820 790 1140 760 L1140 770 C820 800 640 720 470 612 Z" fill="var(--red)"/>
    </svg>

    <div class="portrait" role="img" aria-label="Portrait photo of the insurance advisor in a dark suit and red shirt"></div>

    <address class="contact" style="font-style:normal">
      <p class="contact-name">TOBY HALVERN</p>
      <p class="contact-line">Phone: Cell 555 207 4816</p>
      <p class="contact-line">Email: thalvern@ruralplexadvice.example</p>
    </address>

    <div class="footer-bar"></div>
  </main>
</body>
</html>
```